Vantor Ridge needs a Business Card Design

We need a business card design for an Information Technology company based in Fairfax Virginia called Vantor Ridge. We want the business card to use our logo colors. We need it to be double-sided. The business card needs to look professional but we would like it to be unique. You can get company information from our web site (http://www.vantorridgellc.example).

Target Market(s)

Target market is Government Agencies and Business Professionals.

Industry/Entity Type

Business

Requirements
Must have
• Must have section for company name, company address, company URL, employee name, title, phone and email. Also must have company logo and space for entering logos.

```html
<!DOCTYPE html>
<html lang="en">
<head>
<meta charset="utf-8">
<title>Vantor Ridge — Business Card</title>
<link rel="stylesheet" href="https://fonts.googleapis.com/css2?family=Montserrat:wght@600&family=Questrial&family=Tinos&display=swap">
<style>
  :root {
    --page-bg: #e4e4e6;
    --card-black: #050506;
    --card-black-edge: #1a1a1c;
    --card-blue: #2f3f9c;
    --card-blue-deep: #283a8f;
    --brand-blue: #2d7ed6;
    --mark-blue: #2f4fae;
    --text-blue: #2a68c8;
    --back-text: #4d6fd8;
    --mark-back: #23337f;
  }
  * { margin: 0; padding: 0; box-sizing: border-box; }
  html, body { width: 1200px; height: 750px; overflow: hidden; }
  body {
    background: var(--page-bg);
    position: relative;
  }
  .card {
    position: absolute;
    top: 238px;
    width: 480px;
    height: 274px;
    border-radius: 22px;
    overflow: hidden;
  }
  /* Back side: name & contact */
  .card-back {
    left: 90px;
    background: linear-gradient(200deg, var(--card-blue-deep), var(--card-blue) 70%, #3548a6);
  }
  .back-row {
    position: absolute;
    left: 0; right: 0; top: 116px;
    display: flex;
    align-items: center;
    justify-content: center;
    gap: 14px;
  }
  .person {
    font-family: "Tinos", serif;
    color: var(--back-text);
    text-align: right;
    text-transform: uppercase;
    line-height: 1.05;
  }
  .person-name { font-size: 17px; letter-spacing: 0.5px; }
  .person-title { font-size: 12px; letter-spacing: 0.5px; }
  .brand-square {
    width: 30px; height: 30px;
    background: var(--mark-back);
    flex: none;
  }
  .contact {
    font-family: "Questrial", sans-serif;
    color: var(--back-text);
    font-size: 10px;
    letter-spacing: 1px;
    text-transform: uppercase;
    line-height: 1.5;
  }
  /* Front side: company */
  .card-front {
    left: 630px;
    background: radial-gradient(ellipse at 70% 20%, var(--card-black-edge), var(--card-black) 65%);
  }
  .brand {
    position: absolute;
    left: 70px; top: 96px;
    display: flex;
    align-items: center;
    gap: 14px;
  }
  .brand-front-square {
    width: 38px; height: 38px;
    background: var(--mark-blue);
    flex: none;
  }
  .brand-name {
    font-family: "Montserrat", sans-serif;
    font-weight: 600;
    font-size: 27px;
    color: var(--brand-blue);
    text-transform: uppercase;
    line-height: 1;
  }
  .tagline {
    font-family: "Questrial", sans-serif;
    font-size: 8.5px;
    letter-spacing: 1.2px;
    color: var(--text-blue);
    text-transform: uppercase;
    margin-top: 4px;
  }
  .address {
    position: absolute;
    left: 0; right: 0; top: 160px;
    text-align: center;
    font-family: "Questrial", sans-serif;
    font-size: 11px;
    letter-spacing: 2px;
    color: var(--text-blue);
    line-height: 1.45;
  }
  .website {
    position: absolute;
    left: 0; right: 0; bottom: 20px;
    text-align: center;
    font-family: "Questrial", sans-serif;
    font-size: 8px;
    letter-spacing: 4px;
    color: var(--text-blue);
  }
</style>
</head>
<body>
  <section class="card card-back" aria-label="Business card back">
    <div class="back-row">
      <div class="person">
        <div class="person-name">Your Name</div>
        <div class="person-title">Title</div>
      </div>
      <div class="brand-square"></div>
      <div class="contact">
        <div>Ph. 444-555-555</div>
        <div>Email: yourmail@your.com</div>
      </div>
    </div>
  </section>

  <section class="card card-front" aria-label="Business card front">
    <div class="brand">
      <div class="brand-front-square"></div>
      <div>
        <div class="brand-name">Vantor Ridge</div>
        <div class="tagline">Transforming concepts into solutions</div>
      </div>
    </div>
    <div class="address">
      <div>XXXXX XXXXX XXXXXX</div>
      <div>XXXXX XXXX</div>
      <div>XXXXX - 555-4444</div>
    </div>
    <div class="website">www.yoursite.com</div>
  </section>
</body>
</html>
```